Business Cards for cafe providing speciality coffee and food

I need a business card design for my husband’s businesses. He has two cafes in Brisbane. The business name is Copperleaf Roasting House. They sell high end specialty coffee as well as breakfast and lunch. All the food is cooked fresh, in house and they have strict quality controls for their coffee. I would like the business card to feature the address for both cafes, my husband’s phone number and the business’s instagram. The address for the first is 61 Walden Crescent, Oakvale and the second is 23 Pellow Avenue, Brindlemoor. The Instagram handle is @copperleafroastinghouse and phone number is 0491362847. We already have a business logo that is attached.

Target Market(s)

All ages, higher disposable income and more likely to eat out regularly

Industry/Entity Type

Hospitality

Contact Information for Business Card

Must be suitable for both customers and suppliers

Font styles to use
Sans Serif

Colors

Designer to choose colors to be used in the design.

Requirements
Must have
• Owner’s name: Reid Castell
• Addresses of both cafes: 61 Walden Crescent, Oakvale and 23 Pellow Avenue, Brindlemoor
• Instagram handle: @copperleafroastinghouse
• Contact number: 0491362847
Nice to have
• Business logo

```html
<!DOCTYPE html>
<html lang="en">
<head>
<meta charset="utf-8">
<title>Copperleaf Roasting House – Business Card</title>
<link rel="stylesheet" href="https://fonts.googleapis.com/css2?family=Roboto:wght@500;700&family=Lato:wght@400&display=swap">
<style>
  :root {
    --backdrop: #666666;
    --card-light: #ffffff;
    --card-dark: #000000;
    --ink: #111111;
    --ink-soft: #333333;
    --rule: #d6d6d6;
    --paper-text: #ffffff;
  }
  html, body {
    margin: 0;
    padding: 0;
    width: 1200px;
    height: 900px;
    overflow: hidden;
    background: var(--backdrop);
  }
  .canvas {
    position: relative;
    width: 1200px;
    height: 900px;
  }
  .card {
    position: absolute;
    top: 275px;
    width: 477px;
    height: 294px;
    box-sizing: border-box;
  }
  .card--front {
    left: 120px;
    background: var(--card-light);
    border-radius: 0 55px 0 55px;
  }
  .card--back {
    left: 620px;
    background: var(--card-dark);
    border-radius: 55px 0 55px 0;
  }
  .brand-mark {
    position: absolute;
    width: 150px;
    height: 150px;
    display: flex;
    flex-direction: column;
    align-items: center;
    justify-content: center;
    text-align: center;
    font-family: "Roboto", sans-serif;
    font-weight: 700;
    font-size: 15px;
    line-height: 1.3;
    letter-spacing: 1.5px;
    text-transform: uppercase;
    box-sizing: border-box;
    border-radius: 50%;
  }
  .card--front .brand-mark {
    left: 50px;
    top: 75px;
    color: var(--ink);
    border: 3px solid var(--ink);
  }
  .card--back .brand-mark {
    left: 163px;
    top: 75px;
    color: var(--paper-text);
    border: 3px solid var(--paper-text);
  }
  .divider {
    position: absolute;
    left: 226px;
    top: 70px;
    width: 1px;
    height: 150px;
    background: var(--rule);
  }
  .contact {
    position: absolute;
    left: 250px;
    top: 80px;
    color: var(--ink-soft);
    font-family: "Lato", sans-serif;
    font-size: 13.5px;
  }
  .contact__name {
    margin: 0 0 14px;
    font-family: "Roboto", sans-serif;
    font-weight: 700;
    font-size: 18.5px;
    color: var(--ink);
    letter-spacing: 0.2px;
  }
  .contact__line {
    display: flex;
    align-items: center;
    gap: 5px;
    margin: 0 0 2px;
    line-height: 16px;
  }
  .contact__icon {
    width: 15px;
    height: 15px;
    flex: none;
  }
  .contact__addresses {
    margin-top: 12px;
  }
  .contact__address {
    margin: 0 0 9px;
    line-height: 16px;
  }
</style>
</head>
<body>
<main class="canvas">
  <section class="card card--front">
    <div class="brand-mark">Copperleaf<br>Roasting<br>House</div>
    <div class="divider"></div>
    <div class="contact">
      <h1 class="contact__name">REID CASTELL</h1>
      <p class="contact__line">
        <svg class="contact__icon" viewBox="0 0 16 16" aria-hidden="true">
          <circle cx="8" cy="8" r="8" fill="#111"/>
          <path d="M5 4.2c.4-.3.9-.2 1.1.2l.7 1.3c.2.4.1.8-.2 1l-.5.4c.4.9 1.1 1.6 2 2l.4-.5c.3-.3.7-.4 1-.2l1.3.7c.4.2.5.7.2 1.1l-.5.6c-.4.4-1 .6-1.6.4-2-.7-3.6-2.3-4.3-4.3-.2-.6 0-1.2.4-1.6z" fill="#fff"/>
        </svg>
        0491362847
      </p>
      <p class="contact__line">
        <svg class="contact__icon" viewBox="0 0 16 16" aria-hidden="true">
          <circle cx="8" cy="8" r="8" fill="#111"/>
        </svg>
        @copperleafroastinghouse
      </p>
      <div class="contact__addresses">
        <p class="contact__address">61 Walden Crescent, Oakvale</p>
        <p class="contact__address">23 Pellow Avenue, Brindlemoor</p>
      </div>
    </div>
  </section>
  <section class="card card--back">
    <div class="brand-mark">Copperleaf<br>Roasting<br>House</div>
  </section>
</main>
</body>
</html>
```